new service company in the field of construction seeks to make the Creation of a PPT

We need a PPT format with a cover page a frame for presentation. our company is based in Paris which was named VORENTEX. we just did our logo attached. Our company offers services to manage and control documents that pass on projects in construction (building, infrastructure, energy, oil and gas etc. ..). We use internet systems to help us, design must show insurance, quality, and safety. Customers should build any type of works and can not build without the approved documents. These documents go through multiple validations, and vorentex staff seconded on projects, coordinate these processes and documents, quality documents, to ensure that project deadlines are met and project management sees his project developed within the period, through regular reporting. the services offered by our company help ensure the project of building on time, to ensure the project manager visibility on what e will not, and can act accordingly.

Target Market(s)

general contractor of engineering construction or big business masters lumber wholesale real estate investor, project ownership in the construction sector

Industry/Entity Type

Construction

Contact Information for Business Card

carte rectangulaire petite taille (4X6cm env)
horizontale ou verticale
prendre en compte les éléments suivants :
logo
nom de société
adresse postale (4 lignes)
teléphone:
mail
role (ex : directeur)
in the back : La qualité documentaire de vos projets

Font styles to use
Sans Serif

Colors
34a7d7
85cae6
cee9f5
0592cd

Requirements
Must have
• The project should have 2 sliders: slider 1. Cover Page 2. slider for the content of presentations THE GOAL IS TO HAVE A VISUAL IDENTITY ON PPT, MY BUSINESS CARDS AND LETTERS must stay in mind and colors of the logo that joined the design must be clean and recall the seriousness, ease. the design must take into account the page numbers Tag line: the documentary quality of your projects information such as tagline and writes must be modifiable
Nice to have
• would require the presentation of the figure shows concepts or reporting table THE GOAL IS TO HAVE A VISUAL IDENTITY ON PPT, MY BUSINESS CARDS AND LETTERS
Should not have
• not to building or building in the logo

```html
<!DOCTYPE html>
<html lang="en">
<head>
<meta charset="UTF-8">
<title>VORENTEX – My Identity</title>
<link href="https://fonts.googleapis.com/css2?family=Open+Sans:wght@400;600;700&display=swap" rel="stylesheet">
<style>
  :root {
    --white: #ffffff;
    --ink: #3f3f3f;
    --brand: #2e78b8;
    --header-a: #9fcbd3;
    --header-b: #55a8cb;
    --header-c: #1f74b5;
    --bulb: #8ecbc4;
    --bulb-base: #3a8fc6;
    --tag1: #2479b8; --tag1-accent: #3d97cc;
    --tag2: #66abbd; --tag2-accent: #8ac6c4;
    --tag3: #3e9ac9; --tag3-accent: #5ab0c9;
    --tag4: #8ecbc4; --tag4-accent: #a8dcbb;
  }
  * { margin: 0; padding: 0; box-sizing: border-box; }
  html, body { width: 1200px; height: 662px; overflow: hidden; background: var(--white); }
  .slide {
    position: relative; width: 1200px; height: 662px; overflow: hidden;
    background: var(--white); font-family: "Open Sans", Arial, sans-serif;
  }
  .header-band { position: absolute; left: 0; top: 0; width: 1200px; height: 210px; }
  .slide-title {
    position: absolute; left: 0; right: 0; top: 30px; text-align: center;
    color: var(--white); font-size: 46px; font-weight: 700; letter-spacing: 0.5px;
  }
  .bulb-visual {
    position: absolute; left: 121px; top: 141px; width: 278px; height: 470px;
    background: linear-gradient(180deg, var(--bulb) 0 72%, var(--bulb-base) 72% 100%);
    border-radius: 140px 140px 60px 60px;
  }
  .feature { position: absolute; width: 280px; }
  .feature-1 { left: 484px; top: 220px; --c: var(--tag1); --a: var(--tag1-accent); }
  .feature-2 { left: 806px; top: 220px; --c: var(--tag2); --a: var(--tag2-accent); }
  .feature-3 { left: 484px; top: 435px; --c: var(--tag3); --a: var(--tag3-accent); }
  .feature-4 { left: 806px; top: 435px; --c: var(--tag4); --a: var(--tag4-accent); }
  .feature-tag { position: relative; width: 272px; height: 35px; }
  .feature-tag svg { position: absolute; left: 0; top: 0; }
  .tag-main { fill: var(--c); }
  .tag-accent { fill: var(--a); }
  .feature-label {
    position: absolute; left: 0; top: 0; width: 226px; line-height: 35px;
    text-align: center; color: var(--white); font-weight: 700; font-size: 17px;
  }
  .feature-text {
    margin-top: 22px; color: var(--ink); font-size: 18.5px; line-height: 22px;
  }
  .brand-mark { position: absolute; left: 980px; top: 539px; width: 197px; text-align: center; }
  .brand-dot {
    display: block; width: 50px; height: 50px; margin: 0 auto 6px;
    border-radius: 50%; background: var(--brand);
  }
  .brand-name { color: var(--brand); font-size: 36px; font-weight: 600; line-height: 40px; letter-spacing: 0.5px; }
</style>
</head>
<body>
<main class="slide">
  <svg class="header-band" viewBox="0 0 1200 210" role="img" aria-label="Faceted geometric header pattern in soft teal and blue tones">
    <defs>
      <linearGradient id="headerGradient" x1="0" y1="0" x2="1" y2="0">
        <stop offset="0" stop-color="var(--header-a)"/>
        <stop offset="0.55" stop-color="var(--header-b)"/>
        <stop offset="1" stop-color="var(--header-c)"/>
      </linearGradient>
    </defs>
    <polygon fill="url(#headerGradient)" points="0,0 1200,0 1200,164 1143,202 861,91 750,168 270,100 0,158"/>
  </svg>
  <h1 class="slide-title">MY IDENTITY</h1>

  <div class="bulb-visual" role="img" aria-label="Illustration of a light bulb in mint green with a blue screw base"></div>

  <section class="feature feature-1">
    <div class="feature-tag">
      <svg width="272" height="35"><polygon class="tag-main" points="0,0 226,0 212,35 0,35"/><polygon class="tag-accent" points="235,0 272,0 255,35 221,35"/></svg>
      <span class="feature-label">LOREM IPSUM</span>
    </div>
    <p class="feature-text">Lorem ipsum dolor sit<br>amet consectetur<br>adipiscing elit, sed do<br>eiusmod tempor</p>
  </section>

  <section class="feature feature-2">
    <div class="feature-tag">
      <svg width="272" height="35"><polygon class="tag-main" points="0,0 226,0 212,35 0,35"/><polygon class="tag-accent" points="235,0 272,0 255,35 221,35"/></svg>
      <span class="feature-label">LOREM IPSUM</span>
    </div>
    <p class="feature-text">Lorem ipsum dolor sit<br>amet consectetur<br>adipiscing elit, sed do<br>eiusmod tempor</p>
  </section>

  <section class="feature feature-3">
    <div class="feature-tag">
      <svg width="272" height="35"><polygon class="tag-main" points="0,0 226,0 212,35 0,35"/><polygon class="tag-accent" points="235,0 272,0 255,35 221,35"/></svg>
      <span class="feature-label">LOREM IPSUM</span>
    </div>
    <p class="feature-text">Lorem ipsum dolor sit<br>amet consectetur<br>adipiscing elit, sed do<br>eiusmod tempor</p>
  </section>

  <section class="feature feature-4">
    <div class="feature-tag">
      <svg width="272" height="35"><polygon class="tag-main" points="0,0 226,0 212,35 0,35"/><polygon class="tag-accent" points="235,0 272,0 255,35 221,35"/></svg>
      <span class="feature-label">LOREM IPSUM</span>
    </div>
    <p class="feature-text">Lorem ipsum dolor sit<br>amet consectetur<br>adipiscing elit, sed do<br>eiusmod tempor</p>
  </section>

  <div class="brand-mark">
    <span class="brand-dot"></span>
    <span class="brand-name">VORENTEX</span>
  </div>
</main>
</body>
</html>
```